Design AND code an HTML landing page

A landing page for campaigns and webinars respondents for project www.brevamor-homes.example. We expect the design to be coded. We will provide the copy and content. It will be a simple landing page for a new development project, to capture details of any potential clients showing interest, including any leads generated via webinars.

Broad instructions are as follows:
- It should not have a header or footer. Minimum escape links as possible.
- Create a lead generator box to get e-mails / relevant info of people interested.
- If possible, add a virtual tour (link to host server provided) at the top of the page.
- Content will be provided
- An option to include a link to a ClipVerra video

Target Market(s)

Pre/retiree and retirees

Industry/Entity Type

Real estate development, retirement, relocation, travel and tourism

Coding

Coded - Design and coding required

Font styles to use
Other font styles liked:
• Preferably same as existing site

Colors
FFF300
FFF600
FEFA6F
FFFEC7
FFFEE8

Requirements
Must have
• Simple yet appealing look and feel, within the motif of the project, simple list of questions
Should not have
• Emojis, unrelated graphics, excessive graphics that are not linked to project

```html
<!DOCTYPE html>
<html lang="en">
<head>
<meta charset="utf-8">
<title>Brevamor Homes – Campaigns &amp; Webinars</title>
<link href="https://fonts.googleapis.com/css2?family=Poppins:ital,wght@0,300;0,400;0,500;0,600;1,600&family=Lato:wght@400&display=swap" rel="stylesheet">
<style>
:root{
  --yellow:#f9d40f;
  --yellow-text:#f2c40c;
  --white:#ffffff;
  --ink:#111111;
  --body:#222222;
  --panel:rgba(38,40,44,0.78);
  --field-line:rgba(255,255,255,0.85);
  --footer:#232323;
}
*{box-sizing:border-box;margin:0;padding:0}
html,body{width:1076px;height:1200px;overflow:hidden;background:var(--white)}
body{position:relative;font-family:'Poppins',sans-serif;color:var(--body)}

.hero{position:absolute;left:0;top:0;width:1076px;height:662px;overflow:hidden}
.hero-photo{position:absolute;inset:0;
  background:linear-gradient(180deg,#5f86aa 0%,#8fa6b8 22%,#9a9690 45%,#6e6a60 62%,#4f5a33 78%,#3f5224 100%)}
.hero-shade{position:absolute;inset:0;background:linear-gradient(90deg,rgba(0,0,0,0.15),rgba(0,0,0,0.05) 50%,rgba(0,0,0,0.15))}

.brand{position:absolute;left:67px;top:52px;font-size:30px;font-weight:500;color:var(--white);line-height:40px;letter-spacing:0.3px}

.tour-btn{position:absolute;left:849px;top:51px;width:161px;height:43px;background:var(--yellow);
  color:var(--white);font-size:17px;font-weight:600;display:flex;align-items:center;justify-content:center;text-decoration:none;letter-spacing:0.3px}

.welcome{position:absolute;left:68px;top:298px;color:var(--white)}
.welcome-line{font-size:46px;font-weight:400;line-height:1.1}
.welcome-name{font-size:60px;font-weight:400;color:var(--yellow);line-height:1.05;margin-top:2px;white-space:nowrap}

.contact{position:absolute;left:632px;top:142px;width:378px;height:465px;background:var(--panel);padding:0 30px}
.contact h2{font-size:35px;font-weight:500;color:var(--white);margin-top:18px;line-height:1.2;letter-spacing:0.3px}
.field{width:318px;height:47px;border:1px solid var(--field-line);background:transparent;
  color:var(--white);font-family:'Poppins',sans-serif;font-size:13.5px;padding:0 15px;display:flex;align-items:center;letter-spacing:0.3px}
.field + .field{margin-top:10px}
.contact .first{margin-top:14px}
.field.message{height:85px;align-items:flex-start;padding-top:14px;margin-top:13px}
.submit{margin-top:10px;width:318px;height:47px;background:var(--yellow);color:var(--ink);
  font-size:18px;font-weight:600;display:flex;align-items:center;justify-content:center}

.section-title{position:absolute;top:716px;font-size:26px;font-weight:600;color:var(--ink);letter-spacing:0.2px}
.campaigns-title{left:67px}
.webinars-title{left:552px}

.campaign{position:absolute;left:67px;width:450px;height:127px}
.campaign-photo{position:absolute;left:0;top:0;width:174px;height:127px}
.campaign-one .campaign-photo{background:linear-gradient(180deg,#a9c6de 0%,#6f94aa 35%,#6f7a6a 60%,#55565a 100%)}
.campaign-two .campaign-photo{background:linear-gradient(160deg,#6c7d4a 0%,#3b3d36 45%,#5d6656 75%,#3d9fc6 100%)}
.campaign-body{position:absolute;left:193px;top:-8px;width:260px}
.campaign-body h3{font-size:20px;font-weight:500;color:var(--ink);line-height:1.3;letter-spacing:0.3px}
.campaign-body p{font-size:14px;line-height:25px;margin-top:5px;letter-spacing:0.2px}
.details{display:inline-block;margin-top:4px;font-size:13.5px;font-weight:600;font-style:italic;color:var(--yellow-text);
  text-decoration:none;border-bottom:1px solid var(--yellow-text);line-height:1.25}
.campaign-one{top:772px}
.campaign-two{top:930px}

.webinar{position:absolute;left:552px;top:772px;width:458px;height:285px;
  background:linear-gradient(120deg,#c9c9c4 0%,#8e8f86 40%,#6f89a6 65%,#9a7a55 100%)}
.play{position:absolute;left:202px;top:115px}

.footer{position:absolute;left:0;top:1118px;width:1076px;height:82px;background:var(--footer);
  color:var(--white);font-family:'Lato',sans-serif;font-size:13px;display:flex;align-items:center;justify-content:center}
</style>
</head>
<body>
<section class="hero">
  <div class="hero-photo" role="img" aria-label="Photo of the low-rise apartment development with balconies, lawn and sun loungers under an evening sky"></div>
  <div class="hero-shade"></div>

  <div class="brand">Brevamor Homes</div>

  <a class="tour-btn" href="#">Virtual Tour</a>

  <div class="welcome">
    <div class="welcome-line">Welcome to</div>
    <div class="welcome-name">Brevamor Homes</div>
  </div>

  <form class="contact">
    <h2>Quick Contact</h2>
    <div class="field first">Enter Name</div>
    <div class="field">Enter Email Address</div>
    <div class="field">Phone No</div>
    <div class="field">Subject</div>
    <div class="field message">Message</div>
    <div class="submit">Submit</div>
  </form>
</section>

<h2 class="section-title campaigns-title">Our Campaigns</h2>
<h2 class="section-title webinars-title">Our Webinars</h2>

<article class="campaign campaign-one">
  <div class="campaign-photo" role="img" aria-label="Photo of a rooftop terrace overlooking the town and the sea"></div>
  <div class="campaign-body">
    <h3>Campaign Heading</h3>
    <p>Sed ut perspiciatis unde omnis iste natus error sit voluptatem accus antium doloremque laudantium</p>
    <a class="details" href="#">View Details</a>
  </div>
</article>

<article class="campaign campaign-two">
  <div class="campaign-photo" role="img" aria-label="Aerial photo of the apartment blocks with gardens and a swimming pool"></div>
  <div class="campaign-body">
    <h3>Campaign Heading</h3>
    <p>Sed ut perspiciatis unde omnis iste natus error sit voluptatem accus antium doloremque laudantium</p>
    <a class="details" href="#">View Details</a>
  </div>
</article>

<div class="webinar" role="img" aria-label="Video still of a person with headphones taking notes at a desk during a webinar">
  <svg class="play" width="56" height="56" viewBox="0 0 56 56">
    <circle cx="28" cy="28" r="25" fill="none" stroke="#ffffff" stroke-width="4"/>
    <path d="M21 16 L40 28 L21 40 Z" fill="#ffffff" stroke="#ffffff" stroke-width="3" stroke-linejoin="round"/>
  </svg>
</div>

<footer class="footer">Copyright © 2022, Company Name All Right reserved</footer>
</body>
</html>
```